Tall Reed Software PowerPoint template

We are a software company selling endpoint visibility, access and security technology to enterprise-level IT departments.
Our technology helps organizations gain comprehensive visibility into and control over devices accessing their corporate network so they can quickly identify and address suspicious activity on the network that could lead to potential threats like data breaches.
This technology can cost organizations upwards of $1M - depending on the size of the organization. Our primary clients are Meridian 2,000 companies.
We want a professional, polished PowerPoint template that we can use for all company presentations. Please include:
Title page
Section page
General info page
Thank you page
Logo options and color specs are attached.
Please include our tagline on at least the title page: Discover the edge. Optimize the whole.

```html
<!DOCTYPE html>
<html lang="en">
<head>
<meta charset="utf-8">
<title>Tall Reed Software – Presentation Template</title>
<link rel="stylesheet" href="https://fonts.googleapis.com/css2?family=Jost:wght@500;600&family=Mulish:wght@400;600&display=swap">
<style>
  :root {
    --red: #8f0409;
    --red-band: #a70a10;
    --red-deep: #5a0306;
    --orange: #de8152;
    --orange-title: #ec8a55;
    --white: #ffffff;
    --ink: #4a4a4a;
    --grey-bar: #5e5e5e;
    --stage: #2b2b2b;
    --rule: #f1d2c2;
  }
  * { box-sizing: border-box; margin: 0; padding: 0; }
  html, body { width: 1068px; height: 1200px; overflow: hidden; background: var(--stage); }
  body { font-family: "Mulish", Arial, sans-serif; }
  .deck {
    position: relative; width: 1068px; height: 1200px;
    display: grid; grid-template-columns: 512px 512px; grid-template-rows: 384px 384px 384px;
    gap: 12px 20px; padding: 6px 12px;
  }
  .slide { position: relative; width: 512px; height: 384px; overflow: hidden; }
  .slide--red { background: var(--red); }
  .slide--white { background: var(--white); }

  .footer {
    position: absolute; left: 0; right: 0; bottom: 0; height: 18px;
    background: var(--orange); color: var(--white);
    display: flex; justify-content: space-between; align-items: center;
    padding: 0 6px; font-size: 7.5px; font-weight: 600; text-transform: uppercase;
  }
  .footer .page { text-transform: none; }

  .brand { display: flex; align-items: center; gap: 10px; color: var(--white); }
  .brand-mark { width: 26px; height: 26px; background: currentColor; }
  .brand-name {
    font-family: "Jost", Arial, sans-serif; font-weight: 600;
    font-size: 20px; letter-spacing: 3px; line-height: 1.05; text-transform: uppercase;
  }
  .brand-name span { display: block; font-size: 11px; letter-spacing: 7px; }
  .brand--small { color: var(--red); gap: 6px; }
  .brand--small .brand-mark { width: 12px; height: 12px; background: var(--orange); }
  .brand--small .brand-name { font-size: 11px; letter-spacing: 1.5px; }
  .brand--small .brand-name span { font-size: 6px; letter-spacing: 4px; }

  /* cover */
  .cover-photo { position: absolute; left: 0; top: 0; width: 512px; height: 262px;
    background: radial-gradient(circle at 32% 10%, #fbeeee 0%, #c99797 25%, #8e5555 60%, #4e2525 100%); }
  .cover-band { position: absolute; left: 0; top: 262px; width: 512px; height: 103px; background: var(--red-band);
    border-bottom: 2px solid var(--white); }
  .cover-grey { position: absolute; left: 0; top: 365px; width: 512px; height: 19px; background: var(--grey-bar); }
  .tagline { position: absolute; left: 20px; top: 30px; font-family: "Jost", Arial, sans-serif;
    font-weight: 600; font-size: 17px; line-height: 27px; text-transform: uppercase; }
  .tagline .line-dark { color: var(--red-deep); display: block; }
  .tagline .line-light { color: var(--orange-title); display: block; }
  .cover-band .brand { position: absolute; right: 14px; top: 32px; }

  /* title */
  .title-block { position: absolute; left: 0; right: 0; top: 104px; text-align: center; }
  .title-main { font-family: "Jost", Arial, sans-serif; font-weight: 600; font-size: 23px;
    color: var(--orange-title); text-transform: uppercase; }
  .title-sub { width: 230px; margin: 8px auto 0; color: var(--white); font-size: 8.5px; line-height: 13px; }
  .title-brand { position: absolute; left: 0; right: 0; top: 236px; display: flex; justify-content: center; }

  /* content */
  .content-head { position: absolute; left: 0; right: 0; top: 0; height: 34px;
    border-bottom: 1px solid var(--rule); display: flex; justify-content: space-between; align-items: center;
    padding: 0 8px 0 12px; }
  .content-title { font-family: "Jost", Arial, sans-serif; font-weight: 600; font-size: 20px;
    text-transform: uppercase; color: var(--red); padding-top: 8px; }
  .content-title em { font-style: normal; color: var(--orange-title); }
  .item { position: absolute; }
  .item h3 { font-family: "Mulish", Arial, sans-serif; font-weight: 600; font-size: 11px; color: var(--orange); margin-bottom: 3px; }
  .item p { font-size: 8px; line-height: 12.8px; color: var(--ink); }
  .image-slot { position: absolute; left: 19px; width: 121px; height: 121px; border-radius: 50%;
    background: var(--orange); color: var(--white); display: flex; align-items: center; justify-content: center;
    font-size: 12px; font-weight: 600; }

  /* section */
  .section-icon { position: absolute; left: 225px; top: 130px; }
  .section-title { position: absolute; left: 0; right: 0; top: 210px; text-align: center;
    font-family: "Jost", Arial, sans-serif; font-weight: 600; font-size: 28px; color: var(--orange-title); text-transform: uppercase; }

  /* thanks */
  .thanks-brand { position: absolute; left: 26px; top: 180px; }
  .thanks { position: absolute; left: 277px; top: 162px; }
  .thanks h2 { font-family: "Jost", Arial, sans-serif; font-weight: 600; font-size: 19px; color: var(--orange-title); text-transform: uppercase; margin-bottom: 6px; }
  .thanks p { color: #e7a98a; font-size: 9px; line-height: 13px; }
</style>
</head>
<body>
<main class="deck">

  <section class="slide slide--cover">
    <div class="cover-photo" role="img" aria-label="Photo of a professional woman touching a glowing digital interface"></div>
    <div class="cover-band">
      <p class="tagline"><span class="line-dark">Discover the edge</span><span class="line-light">Optimize the whole</span></p>
      <div class="brand"><span class="brand-mark"></span><p class="brand-name">Tall Reed<span>Software</span></p></div>
    </div>
    <div class="cover-grey"></div>
  </section>

  <section class="slide slide--red">
    <div class="title-block">
      <h1 class="title-main">Project title here</h1>
      <p class="title-sub">Subtext here Subtext here Subtext here Subtext here Subtext here Subtext here Subtext here Subtext here Subtext here</p>
    </div>
    <div class="title-brand"><div class="brand"><span class="brand-mark"></span><p class="brand-name">Tall Reed<span>Software</span></p></div></div>
    <footer class="footer"><span>Copyright text here</span><span class="page">Page : 01</span></footer>
  </section>

  <section class="slide slide--white">
    <header class="content-head">
      <h2 class="content-title">Project <em>title here</em></h2>
      <div class="brand brand--small"><span class="brand-mark"></span><p class="brand-name">Tall Reed<span>Software</span></p></div>
    </header>
    <div class="image-slot" style="top:64px">Images</div>
    <div class="item" style="left:166px; top:64px; width:335px">
      <h3>Subtitle Here</h3>
      <p>Odio possim splendide sea cu. Qui nibh mazim insolens ei, tritani suscipit petentium vis ut. His ex reque dissentiet. Mel vocent numquam et, cetero vocent abhorreant cum ut, sit dictas vivendum eu. Ei eos officiis eleifend expetenda, per ei adhuc decore euismod, quando equidem mei an. Novum adipiscing mea ad. Odio possim splendide sea cu. Qui nibh mazim insolens ei, tritani suscipit petentium vis ut. His ex reque dissentiet. Mel vocent numquam et, cetero vocent abhorreant cum ut, sit dictas vivendum eu. Ei eos officiis eleifend expetenda, per ei adhuc decore euismod,</p>
    </div>
    <div class="image-slot" style="top:218px">Images</div>
    <div class="item" style="left:166px; top:218px; width:335px">
      <h3>Subtitle Here</h3>
      <p>Odio possim splendide sea cu. Qui nibh mazim insolens ei, tritani suscipit petentium vis ut. His ex reque dissentiet. Mel vocent numquam et, cetero vocent abhorreant cum ut, sit dictas vivendum eu. Ei eos officiis eleifend expetenda, per ei adhuc decore euismod, quando equidem mei an. Novum adipiscing mea ad. Odio possim splendide sea cu. Qui nibh mazim insolens ei, tritani suscipit petentium vis ut. His ex reque dissentiet. Mel vocent numquam et, cetero vocent abhorreant cum ut, sit dictas vivendum eu. Ei eos officiis eleifend expetenda, per ei adhuc decore euismod,</p>
    </div>
    <footer class="footer"><span>Copyright text here</span><span class="page">Page : 01</span></footer>
  </section>

  <section class="slide slide--white">
    <header class="content-head">
      <h2 class="content-title">Project <em>title here</em></h2>
      <div class="brand brand--small"><span class="brand-mark"></span><p class="brand-name">Tall Reed<span>Software</span></p></div>
    </header>
    <div class="item" style="left:26px; top:62px; width:460px">
      <h3>Subtitle Here</h3>
      <p>Odio possim splendide sea cu. Qui nibh mazim insolens ei, tritani suscipit petentium vis ut. His ex reque dissentiet. Mel vocent numquam et, cetero vocent abhorreant cum ut, sit dictas vivendum eu. Ei eos officiis eleifend expetenda, per ei adhuc decore euismod, quando equidem mei an. Novum adipiscing mea ad, soluta ponderum urbanitas nec ea.</p>
    </div>
    <div class="item" style="left:26px; top:165px; width:460px">
      <h3>Subtitle Here</h3>
      <p>Odio possim splendide sea cu. Qui nibh mazim insolens ei, tritani suscipit petentium vis ut. His ex reque dissentiet. Mel vocent numquam et, cetero vocent abhorreant cum ut, sit dictas vivendum eu. Ei eos officiis eleifend expetenda, per ei adhuc decore euismod, quando equidem mei an. Novum adipiscing mea ad, soluta ponderum urbanitas nec ea.</p>
    </div>
    <div class="item" style="left:26px; top:256px; width:460px">
      <h3>Subtitle Here</h3>
      <p>Odio possim splendide sea cu. Qui nibh mazim insolens ei, tritani suscipit petentium vis ut. His ex reque dissentiet. Mel vocent numquam et, cetero vocent abhorreant cum ut, sit dictas vivendum eu. Ei eos officiis eleifend expetenda, per ei adhuc decore euismod, quando equidem mei an. Novum adipiscing mea ad, soluta ponderum urbanitas nec ea.</p>
    </div>
    <footer class="footer"><span>Copyright text here</span><span class="page">Page : 01</span></footer>
  </section>

  <section class="slide slide--red">
    <svg class="section-icon" width="60" height="60" viewBox="0 0 60 60" aria-hidden="true">
      <circle cx="30" cy="30" r="28" fill="none" stroke="#c2381f" stroke-width="2"/>
      <path d="M30 14a11 11 0 0 0-6 20v5h12v-5a11 11 0 0 0-6-20z" fill="none" stroke="#e8a080" stroke-width="1.5"/>
      <path d="M25 42h10M26 45h8M27 29l3 4 3-4M30 33v6" fill="none" stroke="#e8a080" stroke-width="1.5"/>
    </svg>
    <h2 class="section-title">Slide section slide</h2>
    <footer class="footer"><span>Copyright text here</span><span class="page">Page : 01</span></footer>
  </section>

  <section class="slide slide--red">
    <div class="brand thanks-brand"><span class="brand-mark"></span><p class="brand-name">Tall Reed<span>Software</span></p></div>
    <div class="thanks">
      <h2>Thanks for your time</h2>
      <p>Contact Details here Contact Details here<br>Contact Details here Contact Details here<br>Contact Details here Contact Details here<br>Contact Details here Contact Details here</p>
    </div>
    <footer class="footer"><span>Copyright text here</span><span class="page">Page : 01</span></footer>
  </section>

</main>
</body>
</html>
```